A world class design for a " Discount services provider"
Brightfold Savings Network International
A world class design for a " Discount services provider" - Financial Services
Creative Brief
Simple
Kemi ARUBA
Managing Partner
Suite 204, 306 & 118, Corlenne Plaza, Opp. Former Harbour Works Bureau, Tesvara Crescent , Zone 8, Ilumo Abuja - FCT
infokemiaruba@brightfoldmail.example
www.brightfoldsavingsnet.example
The back of the business card should carry my detailed imformation, while the front should carry only the company's designed logo and colour.
Tavolin Tavolin
Dear Designers, Thank you for the wonderful work you have submitted so far. Looking forward to see more beautiful and creative designs though. Great minds!
Dear Designers, Please remember that I also need the following Stationary designs in addtion to the business card design. 1. Letterhead (A4 Size 210mm x 297mm) 2. Envelope (C4 Size 229mmx324mm) 3. Email Signature

```html
<!DOCTYPE html>
<html lang="en">
<head>
<meta charset="utf-8">
<title>Brightfold Savings Network International – Business Card</title>
<link rel="stylesheet" href="https://fonts.googleapis.com/css2?family=Arimo:wght@400;700&family=Tinos:wght@400&display=swap">
<style>
  :root {
    --stage: #e9ebef;
    --card: #ffffff;
    --blue-deep: #1a3a9c;
    --blue-light: #4d93e3;
    --ink: #111111;
    --text: #2a2a2a;
    --brand: #2a3f8f;
    --rule: #2f5fc4;
  }
  * { box-sizing: border-box; margin: 0; padding: 0; }
  html, body { width: 1200px; height: 782px; overflow: hidden; }
  body {
    background: var(--stage);
    display: flex;
    align-items: center;
    justify-content: center;
    gap: 40px;
    font-family: "Arimo", Arial, sans-serif;
  }
  .card {
    position: relative;
    width: 540px;
    height: 310px;
    background: var(--card);
    border-radius: 16px;
    overflow: hidden;
    box-shadow: 0 4px 14px rgba(0,0,0,.12);
  }
  .card__band { position: absolute; inset: 0; width: 100%; height: 100%; }
  .brand {
    position: absolute;
    display: flex;
    align-items: center;
    gap: 10px;
  }
  .brand__dot {
    width: 34px; height: 34px;
    border-radius: 50%;
    background: var(--blue-deep);
    flex: none;
  }
  .brand__name {
    font-family: "Tinos", "Times New Roman", serif;
    font-size: 15px;
    line-height: 1.2;
    text-transform: uppercase;
    color: var(--brand);
    letter-spacing: .3px;
  }
  .card--front .brand { left: 56px; top: 142px; }
  .card--back .brand { left: 34px; top: 170px; }
  .card--back .brand__name { font-size: 12.5px; max-width: 190px; }
  .holder {
    position: absolute;
    right: 26px; top: 52px;
    text-align: right;
    color: #fff;
  }
  .holder__name { font-size: 16px; font-weight: 700; }
  .holder__role { font-size: 13px; margin-top: 2px; }
  .divider {
    position: absolute;
    left: 258px; top: 160px;
    width: 2px; height: 118px;
    background: var(--rule);
  }
  .contact {
    position: absolute;
    left: 272px; top: 160px;
    list-style: none;
    font-size: 12.5px;
    line-height: 19px;
    color: var(--text);
  }
  .contact li { display: flex; align-items: center; gap: 6px; }
  .contact svg { width: 12px; height: 12px; fill: var(--blue-deep); flex: none; }
</style>
</head>
<body>

  <section class="card card--front" aria-label="Business card front">
    <svg class="card__band" viewBox="0 0 540 310" preserveAspectRatio="none" aria-hidden="true">
      <defs>
        <linearGradient id="bandFront" x1="0" y1="0" x2="1" y2="0">
          <stop offset="0" stop-color="#4d93e3"/>
          <stop offset="1" stop-color="#1a3a9c"/>
        </linearGradient>
      </defs>
      <path d="M0 0 H540 V92 C420 40 200 28 0 44 Z" fill="url(#bandFront)"/>
      <path d="M0 54 C200 38 420 50 540 104 V114 C420 62 200 48 0 60 Z" fill="var(--ink)"/>
    </svg>
    <div class="brand">
      <span class="brand__dot"></span>
      <span class="brand__name">Brightfold Savings Network International</span>
    </div>
  </section>

  <section class="card card--back" aria-label="Business card back">
    <svg class="card__band" viewBox="0 0 540 310" preserveAspectRatio="none" aria-hidden="true">
      <defs>
        <linearGradient id="bandBack" x1="0" y1="0" x2="1" y2="0">
          <stop offset="0" stop-color="#4d93e3"/>
          <stop offset="1" stop-color="#1a3a9c"/>
        </linearGradient>
      </defs>
      <path d="M0 0 H540 V124 C430 62 220 22 0 26 Z" fill="url(#bandBack)"/>
      <path d="M0 34 C220 30 430 70 540 134 V144 C430 82 220 42 0 42 Z" fill="var(--ink)"/>
    </svg>
    <div class="holder">
      <p class="holder__name">Arlo Fenwick-Dane</p>
      <p class="holder__role">Consultant</p>
    </div>
    <div class="brand">
      <span class="brand__dot"></span>
      <span class="brand__name">Brightfold Savings Network International</span>
    </div>
    <span class="divider"></span>
    <ul class="contact">
      <li>047,12th floor,Corlenne Plaza</li>
      <li>Road ILM</li>
      <li><svg viewBox="0 0 12 12"><path d="M2.5 1 L4.5 1 L5.5 3.5 L4.2 4.5 C4.8 5.9 6.1 7.2 7.5 7.8 L8.5 6.5 L11 7.5 V9.5 C11 10.3 10.3 11 9.5 11 C5 11 1 7 1 2.5 C1 1.7 1.7 1 2.5 1 Z"/></svg>014 552 0318</li>
      <li><svg viewBox="0 0 12 12"><path d="M3.5 0.5 H8.5 A1 1 0 0 1 9.5 1.5 V10.5 A1 1 0 0 1 8.5 11.5 H3.5 A1 1 0 0 1 2.5 10.5 V1.5 A1 1 0 0 1 3.5 0.5 Z M4 2 V9 H8 V2 Z"/></svg>014 552 0391</li>
      <li><svg viewBox="0 0 12 12"><path d="M1 2.5 H11 V9.5 H1 Z M1.6 3 L6 6.4 L10.4 3 Z" fill-rule="evenodd"/></svg>arlo@brightfoldmail.example</li>
      <li>www.brightfoldsavingsnet.example</li>
    </ul>
  </section>

</body>
</html>
```